Fun Dry Cleaners Business Flyer

We need a 5.5x8.5 business flyer designed for a new dry cleaners based in Texas called "Copperleaf Dry Cleaners". The flyer needs to be 2 sided (no fold) with the front side containing advertising information (slogan, hours of operation, address, etc...) along with the attached logo. The back will need to include the services and prices. The dry cleaners is a sports themed dry cleaners and we occasionally give away free game tickets (pro football, basketball, baseball, college sports tickets and memorabilia also). The design should be fun like the logo but also professional and appealing. We have no particular restrictions on the colors to be used.

The following should be included

Address - 418 N Bramble Ln
Waco, TX, 76704

Two Day Service
Dry Cleaning
Shirts - $1.50
Complete Suits - $9.99
Blouse - $3.00
Jeans/Pants - $4.00
Jackets - $5.00
Alterations
and More...

Hours of Operation: Monday - Friday 7 am - 6pm
Saturday 10am - 4pm
Sunday - Closed

Target Market(s)

Adults 21 and over
Business Professionals
People who go to Church etc...
Students

Industry/Entity Type

Dry Cleaner

Font styles to use
Serif
Sans Serif
Decorative

Colors

Designer to choose colors to be used in the design.

Requirements
Must have
• Logo should be incorporated within the flyer and naturally flow with the design
• The following should be included
• Address - 418 N Bramble Ln
• Waco, TX, 76704
• Two Day Service
• Dry Cleaning
• Shirts $1.25
• Complete Suits $9.99
• Jeans $3.99
• Slacks $3.99
• Sport Coats $3..99
• Blouses $2.99
• Pullovers $3.49
• Dresses $9.99
• Alterations
• and More...
• Hours of Operation: Monday - Friday 7 am - 6pm
• Saturday 10am - 4pm
• Sunday - Closed
• Phone Number - 254-618-5207
Nice to have
• Fun Design but professional, nice color scheme and flow, address should be visible and not hidden on the flyer

```html
<!DOCTYPE html>
<html lang="en">
<head>
<meta charset="utf-8">
<title>Copperleaf Dry Cleaners Flyer</title>
<link href="https://fonts.googleapis.com/css2?family=Bubblegum+Sans&display=swap" rel="stylesheet">
<style>
  :root {
    --backdrop: #2f3336;
    --paper: #ffffff;
    --green-deep: #07833a;
    --green-mid: #14b53a;
    --green-bright: #3fe03a;
    --lime: #d8ef2a;
    --ink: #000000;
    --yellow: #f2ee23;
    --white: #ffffff;
    --blue: #1d8fe8;
    --cyan: #1cd6f2;
  }
  * { box-sizing: border-box; margin: 0; padding: 0; }
  html, body { width: 1076px; height: 1200px; overflow: hidden; }
  body {
    background: var(--backdrop);
    position: relative;
    font-family: "Bubblegum Sans", sans-serif;
    color: var(--white);
  }
  .flyer {
    position: absolute;
    top: 238px;
    width: 452px;
    height: 698px;
    background: var(--paper);
    overflow: hidden;
  }
  .flyer--front { left: 54px; }
  .flyer--back { left: 542px; }
  .flyer__field {
    position: absolute;
    left: 15px; top: 15px; right: 13px; bottom: 13px;
    overflow: hidden;
    background:
      radial-gradient(ellipse at 88% 48%, var(--lime) 0%, rgba(216,239,42,0) 35%),
      linear-gradient(160deg, var(--green-bright) 0%, var(--green-mid) 45%, var(--green-deep) 100%);
  }
  .flyer--back .flyer__field { bottom: 0; }

  .illustration { position: absolute; }
  .front-art {
    left: 0; top: 40px; width: 100%; height: 370px;
    background: linear-gradient(120deg, rgba(28,214,242,.5), rgba(29,143,232,.45) 60%, rgba(0,0,0,.3));
    border-radius: 36px;
  }
  .back-art {
    left: 0; top: 515px; width: 100%; height: 168px;
    background: linear-gradient(110deg, var(--cyan), var(--blue));
    border-radius: 60px 60px 0 0;
  }

  .brand {
    position: absolute;
    display: flex; flex-direction: column; align-items: center; justify-content: center;
    text-align: center;
  }
  .brand__disc {
    border-radius: 50%;
    background: var(--green-deep);
    border: 4px solid var(--white);
  }
  .brand__name { color: var(--white); line-height: 1; }
  .flyer--front .brand { left: 41px; top: 115px; width: 340px; }
  .flyer--front .brand__disc { width: 120px; height: 120px; margin-bottom: 14px; }
  .flyer--front .brand__name { font-size: 50px; }

  .front-panel {
    position: absolute;
    left: 0; top: 403px; width: 100%; height: 232px;
    background: var(--ink);
    transform: skewY(-4deg);
    transform-origin: left top;
  }
  .tagline {
    position: absolute; left: 0; right: 0; top: 14px;
    text-align: center; font-size: 38px; letter-spacing: 1px;
  }
  .info-row {
    position: absolute; left: 0; right: 0; top: 74px; height: 86px;
    border-top: 4px solid var(--green-mid);
    border-bottom: 4px solid var(--green-mid);
  }
  .address {
    position: absolute; left: 0; top: 0; width: 238px; height: 78px;
    border-right: 4px solid var(--green-mid);
    color: var(--yellow); font-size: 23px; line-height: 1.15;
    padding: 12px 0 0 42px;
  }
  .hours {
    position: absolute; left: 250px; top: 6px; right: 6px;
    font-size: 11px; line-height: 1.4;
  }
  .hours__title { color: var(--yellow); font-size: 15px; line-height: 1.1; }
  .phones {
    position: absolute; left: 0; right: 0; top: 176px;
    text-align: center; font-size: 20px; letter-spacing: .5px; white-space: nowrap;
  }
  .phones .sep { margin: 0 14px; }

  .back-column {
    position: absolute;
    left: 93px; top: 0; width: 236px; height: 550px;
    background: var(--ink);
  }
  .flyer--back .brand { left: 0; top: 20px; width: 236px; }
  .flyer--back .brand__disc { width: 86px; height: 86px; margin-bottom: 10px; }
  .flyer--back .brand__name { font-size: 32px; }
  .price-list {
    position: absolute; left: 0; right: 0; top: 228px;
    list-style: none; text-align: center;
    font-size: 21px; line-height: 26.5px;
  }
  .price-list__title { color: var(--yellow); font-size: 29px; line-height: 1; margin-bottom: 10px; }
</style>
</head>
<body>

<section class="flyer flyer--front" aria-label="Flyer front">
  <div class="flyer__field">
    <div class="illustration front-art" role="img" aria-label="Cartoon shirt character running with legs and football, in blue and black"></div>
    <div class="brand">
      <div class="brand__disc"></div>
      <div class="brand__name">Copperleaf<br>Dry Cleaners</div>
    </div>
    <div class="front-panel">
      <div class="tagline">TWO DAY SERVICE</div>
      <div class="info-row">
        <div class="address">418 N Bramble Ln<br>Waco, TX, 76704</div>
        <div class="hours">
          <div class="hours__title">Hours of Operation:</div>
          Monday - Friday 7 am - 6pm<br>
          Saturday 10am - 4pm<br>
          Sunday - Closed
        </div>
      </div>
      <div class="phones">254-618-5207<span class="sep">•</span>254-618-5208</div>
    </div>
  </div>
</section>

<section class="flyer flyer--back" aria-label="Flyer back">
  <div class="flyer__field">
    <div class="back-column">
      <div class="brand">
        <div class="brand__disc"></div>
        <div class="brand__name">Copperleaf<br>Dry Cleaners</div>
      </div>
      <ul class="price-list">
        <li class="price-list__title">Dry Cleaning</li>
        <li>Shirts - $1.50</li>
        <li>Complete Suits - $9.99</li>
        <li>Blouse - $3.00</li>
        <li>Jeans/Pants - $4.00</li>
        <li>Jackets - $5.00</li>
        <li>Alterations</li>
        <li>and More...</li>
      </ul>
    </div>
    <div class="illustration back-art" role="img" aria-label="Close-up of a blue cartoon shirt diving across the bottom"></div>
  </div>
</section>

</body>
</html>
```